Stitch Haven web site

I have been running an online business for 6 years.
www.stitchhaven.com.au I specialise in ribbons, buttons and unique craft materials. I sell online to individuals and shops with seperate retail and wholesale sites. The web page I'd like redesigned is my retail site.

It needs a clean, fresh look. I've recently had a new logo designed (thanks pixel guild!) and want the web site to incorporate the new design and colour scheme of black and white. (new logo attached as a file)

I no longer want the page with the large image www.stitchhaven.com.au I want to have the first page as the retail shop homepage.
http://www.stitchhaven.com.au/index.php so this page needs to have all the links

I want to the look to be fresh, modern and clear. It needs to be quick to load.

Notes from my IT guru: They need to know that the following tend to remain static with just the content section changing on each page; Header Left column (but different in the cart) right column (if required) footer
Updates

Thanks for your designs. 1/3 of my users use mobile devices so please take that into consideration. I would like the logo to be incorporated into the design and be a prominent feature (most have just used it as a tiny image in the top left corner. I would like it to be larger and more prominent.  thanks                                   

Thanks to all the designers who have submitted. Can you please add  'Boutique craft supplies' near the logo. That is my tag line. Thanks

Target Market(s)

Crafty females of all ages

Industry/Entity Type

Business

Requirements
Must have
• links to;
blog
gallery
chatterbook
snapboard
wholesale
space for an image which I change approx every 2 weeks
about Stitch Haven
contact
privacy policy
terms and conditions
newsletter sign up
shipping info
product search
Nice to have
• I am not sure if I want product images on the homepage? I have attached a few images.
Should not have
• not too much colour - I hate the green border I have now

```html
<!DOCTYPE html>
<html lang="en">
<head>
<meta charset="utf-8">
<title>Stitch Haven – Boutique craft supplies</title>
<link rel="stylesheet" href="https://fonts.googleapis.com/css2?family=Arimo:wght@400;700&display=swap">
<style>
:root{
  --page-bg:#f5f5f5;
  --line:#dcdcdc;
  --ink:#111111;
  --text:#444444;
  --muted:#777777;
  --band:#e7e7e7;
  --black:#0d0d0d;
  --green-top:#8fcf1a;
  --green-bottom:#5a9a06;
  --nav-active:#9bdc1c;
  --white:#ffffff;
}
*{box-sizing:border-box;margin:0;padding:0}
html,body{width:1034px;height:1200px;overflow:hidden;background:var(--page-bg)}
body{font-family:"Arimo",Arial,sans-serif;color:var(--text)}
.site{position:relative;width:1000px;height:1160px;transform:scale(1.034);transform-origin:0 0}
.abs{position:absolute}

/* sidebar */
.sidebar{left:132px;top:0;width:224px;height:1090px;border-left:1px solid var(--line);border-right:1px solid var(--line)}
.brand{position:absolute;left:0;top:0;width:224px;height:155px;display:flex;align-items:center;justify-content:center;gap:10px}
.brand-dot{width:14px;height:14px;border-radius:50%;background:var(--ink)}
.brand-name{font-size:28px;font-weight:700;color:var(--ink);letter-spacing:-.3px}
.cat-list{position:absolute;left:0;top:157px;width:223px;list-style:none}
.cat-list li{height:26.4px;border-bottom:1px solid var(--line);display:flex;align-items:center;font-size:11px;color:#555}
.cat-list li.current{background:#e9e9e9;color:var(--ink)}
.cat-list svg{margin:0 11px 0 10px}
.side-head{position:absolute;left:0;width:223px;height:26px;background:var(--black);color:var(--white);font-size:15px;line-height:26px;padding-left:8px}
.side-text{position:absolute;left:8px;font-size:12px;color:#333}
.field{position:absolute;left:9px;width:206px;height:19px;border:1px solid #cfcfcf;background:var(--white);font-size:10px;color:#999;line-height:17px;padding-left:6px}
.btn{position:absolute;background:linear-gradient(var(--green-top),var(--green-bottom));color:var(--white);font-size:10px;text-transform:uppercase;text-align:center}
.social{position:absolute;top:1040px;width:100px;text-align:center;font-size:10px;color:#888;text-transform:uppercase}
.social .icon{width:30px;height:30px;border-radius:50%;margin:0 auto 10px}

/* header */
.tagline{left:372px;top:28px;font-size:15px;font-weight:700;color:var(--ink);text-decoration:underline}
.event{left:372px;top:48px;font-size:11px;line-height:13.5px;color:#555}
.search{left:650px;top:30px;width:215px;height:17px;border:1px solid #cfcfcf;background:var(--white);font-size:10px;color:#999;line-height:15px;padding-left:4px}
.search-btn{position:absolute;right:-1px;top:-1px;width:22px;height:17px;background:var(--black);display:flex;align-items:center;justify-content:center}
.phone{left:650px;top:54px;display:flex;align-items:center;gap:8px;font-size:14px;color:var(--ink)}
.cart{left:765px;top:55px;display:flex;align-items:center;gap:8px;font-size:10px;color:var(--ink)}
.cart span{color:#888;font-size:12px}

.main-nav{left:372px;top:106px;width:493px;height:31px;background:linear-gradient(#2a2a2a,#050505);border-top:2px solid #000;display:flex}
.main-nav a{flex:1;color:#ddd;font-size:11px;text-decoration:none;display:flex;align-items:center;justify-content:center;border-right:1px dashed #555}
.main-nav a:last-child{border-right:0}
.main-nav a.active{color:var(--nav-active)}

.feature{left:372px;top:154px;width:493px;height:282px;border:1px solid #999;background:linear-gradient(135deg,#eaeaf0 0%,#d9c9ee 40%,#f3e3a6 65%,#eec9d6 85%,#e8e8e8 100%)}
.dots{left:372px;top:449px;display:flex;gap:5px}
.dots i{width:7px;height:7px;background:#dcdcdc}
.dots i.on{background:var(--black)}

.section-head{left:372px;top:474px;width:493px;height:30px;background:var(--band);font-size:17px;color:var(--ink);line-height:30px;padding-left:6px}

.card{position:absolute;width:146px;height:246px;border:1px solid #cfcfcf;background:var(--page-bg);text-align:center}
.card .photo{position:absolute;left:15px;top:10px;width:114px;height:120px;border:1px solid #ccc}
.card h3{position:absolute;top:140px;width:100%;font-size:13px;font-weight:400;color:var(--ink)}
.card p{position:absolute;top:155px;width:100%;font-size:10.5px;color:var(--muted)}
.card .price{position:absolute;left:0;top:176px;width:100%;height:27px;background:var(--band);font-size:15px;color:var(--ink);line-height:27px}
.card .btn{left:22px;top:213px;width:101px;height:22px;line-height:22px}
.rule{left:372px;top:795px;width:493px;height:1px;background:var(--line)}

.footer{left:132px;top:1090px;width:733px;height:56px;background:linear-gradient(#2b2b2b,#000);border-top:2px dashed #555;text-align:center}
.footer-links{margin-top:11px;font-size:10.5px;color:#ccc}
.footer-links a{color:#ccc;text-decoration:none;padding:0 8px;border-right:1px solid #666}
.footer-links a:last-child{border-right:0}
.footer-links a.active{color:var(--white);text-decoration:underline}
.copyright{margin-top:6px;font-size:10.5px;color:#ccc}
.copyright b{color:var(--white)}
</style>
</head>
<body>
<div class="site">

  <aside class="abs sidebar">
    <div class="brand"><span class="brand-dot"></span><span class="brand-name">Stitch Haven</span></div>
    <ul class="cat-list">
      <li class="current"><svg width="10" height="8" viewBox="0 0 10 8"><path d="M1 1l3 3-3 3M5 1l3 3-3 3" fill="none" stroke="#333" stroke-width="1.5"/></svg>New Products</li>
      <li><svg width="10" height="8" viewBox="0 0 10 8"><path d="M1 1l3 3-3 3M5 1l3 3-3 3" fill="none" stroke="#555" stroke-width="1.5"/></svg>** Clearance **</li>
      <li><svg width="10" height="8" viewBox="0 0 10 8"><path d="M1 1l3 3-3 3M5 1l3 3-3 3" fill="none" stroke="#555" stroke-width="1.5"/></svg>Adhesives</li>
      <li><svg width="10" height="8" viewBox="0 0 10 8"><path d="M1 1l3 3-3 3M5 1l3 3-3 3" fill="none" stroke="#555" stroke-width="1.5"/></svg>Buttons</li>
      <li><svg width="10" height="8" viewBox="0 0 10 8"><path d="M1 1l3 3-3 3M5 1l3 3-3 3" fill="none" stroke="#555" stroke-width="1.5"/></svg>Card Kits</li>
      <li><svg width="10" height="8" viewBox="0 0 10 8"><path d="M1 1l3 3-3 3M5 1l3 3-3 3" fill="none" stroke="#555" stroke-width="1.5"/></svg>Charms</li>
      <li><svg width="10" height="8" viewBox="0 0 10 8"><path d="M1 1l3 3-3 3M5 1l3 3-3 3" fill="none" stroke="#555" stroke-width="1.5"/></svg>Chipboard</li>
      <li><svg width="10" height="8" viewBox="0 0 10 8"><path d="M1 1l3 3-3 3M5 1l3 3-3 3" fill="none" stroke="#555" stroke-width="1.5"/></svg>Christmas</li>
      <li><svg width="10" height="8" viewBox="0 0 10 8"><path d="M1 1l3 3-3 3M5 1l3 3-3 3" fill="none" stroke="#555" stroke-width="1.5"/></svg>Embellishments</li>
      <li><svg width="10" height="8" viewBox="0 0 10 8"><path d="M1 1l3 3-3 3M5 1l3 3-3 3" fill="none" stroke="#555" stroke-width="1.5"/></svg>Embossing Folders</li>
      <li><svg width="10" height="8" viewBox="0 0 10 8"><path d="M1 1l3 3-3 3M5 1l3 3-3 3" fill="none" stroke="#555" stroke-width="1.5"/></svg>Flowers and Leaves</li>
      <li><svg width="10" height="8" viewBox="0 0 10 8"><path d="M1 1l3 3-3 3M5 1l3 3-3 3" fill="none" stroke="#555" stroke-width="1.5"/></svg>inks, mists and masks</li>
      <li><svg width="10" height="8" viewBox="0 0 10 8"><path d="M1 1l3 3-3 3M5 1l3 3-3 3" fill="none" stroke="#555" stroke-width="1.5"/></svg>Lace</li>
      <li><svg width="10" height="8" viewBox="0 0 10 8"><path d="M1 1l3 3-3 3M5 1l3 3-3 3" fill="none" stroke="#555" stroke-width="1.5"/></svg>Miscellaneous</li>
      <li><svg width="10" height="8" viewBox="0 0 10 8"><path d="M1 1l3 3-3 3M5 1l3 3-3 3" fill="none" stroke="#555" stroke-width="1.5"/></svg>Paper</li>
      <li><svg width="10" height="8" viewBox="0 0 10 8"><path d="M1 1l3 3-3 3M5 1l3 3-3 3" fill="none" stroke="#555" stroke-width="1.5"/></svg>Punches</li>
      <li><svg width="10" height="8" viewBox="0 0 10 8"><path d="M1 1l3 3-3 3M5 1l3 3-3 3" fill="none" stroke="#555" stroke-width="1.5"/></svg>Ribbon Club</li>
      <li><svg width="10" height="8" viewBox="0 0 10 8"><path d="M1 1l3 3-3 3M5 1l3 3-3 3" fill="none" stroke="#555" stroke-width="1.5"/></svg>Ribbons</li>
      <li><svg width="10" height="8" viewBox="0 0 10 8"><path d="M1 1l3 3-3 3M5 1l3 3-3 3" fill="none" stroke="#555" stroke-width="1.5"/></svg>Ribbons - organza</li>
      <li><svg width="10" height="8" viewBox="0 0 10 8"><path d="M1 1l3 3-3 3M5 1l3 3-3 3" fill="none" stroke="#555" stroke-width="1.5"/></svg>Ric Rac</li>
      <li><svg width="10" height="8" viewBox="0 0 10 8"><path d="M1 1l3 3-3 3M5 1l3 3-3 3" fill="none" stroke="#555" stroke-width="1.5"/></svg>Sequins</li>
      <li><svg width="10" height="8" viewBox="0 0 10 8"><path d="M1 1l3 3-3 3M5 1l3 3-3 3" fill="none" stroke="#555" stroke-width="1.5"/></svg>Stamps</li>
      <li><svg width="10" height="8" viewBox="0 0 10 8"><path d="M1 1l3 3-3 3M5 1l3 3-3 3" fill="none" stroke="#555" stroke-width="1.5"/></svg>Stickers</li>
      <li><svg width="10" height="8" viewBox="0 0 10 8"><path d="M1 1l3 3-3 3M5 1l3 3-3 3" fill="none" stroke="#555" stroke-width="1.5"/></svg>Washi tape</li>
    </ul>

    <h2 class="side-head" style="top:807px;font-weight:400">News Letter</h2>
    <p class="side-text" style="top:846px">Subscribe to our mailing list below:</p>
    <div class="field" style="top:873px">Enter your name ...</div>
    <div class="field" style="top:902px">Enter your Email ...</div>
    <div class="btn" style="left:9px;top:937px;width:45px;height:22px;line-height:22px;font-size:11px">Join</div>

    <h2 class="side-head" style="top:982px;font-weight:400">Follow Us</h2>
    <div class="abs" style="left:106px;top:1020px;width:1px;height:55px;background:var(--line)"></div>
    <div class="social" style="left:5px;top:1024px"><div class="icon" style="background:#3b5a98"></div>CHATTERBOOK</div>
    <div class="social" style="left:107px;top:1024px"><div class="icon" style="background:#c8232c"></div>SNAPBOARD</div>
  </aside>

  <header>
    <h1 class="abs tagline">Boutique craft supplies</h1>
    <p class="abs event">Harbour Craft &amp; Quilt Fair 22-26th May,<br>Harbour Convention &amp; Exhibition Centre<br>STAND G32</p>
    <div class="abs search">Search Stitch Haven ...
      <span class="search-btn"><svg width="11" height="11" viewBox="0 0 11 11"><circle cx="4.5" cy="4.5" r="3.3" fill="none" stroke="#fff" stroke-width="1.6"/><path d="M7 7l3 3" stroke="#fff" stroke-width="2"/></svg></span>
    </div>
    <div class="abs phone"><svg width="8" height="16" viewBox="0 0 8 16"><path d="M3 1C1 2 1 14 3 15l2-1-1-4H3V6h1l1-4z" fill="#bbb"/></svg>555 019 274</div>
    <div class="abs cart"><svg width="18" height="14" viewBox="0 0 18 14"><path d="M1 1h3l2 8h9l2-6H5" fill="none" stroke="#bbb" stroke-width="1.4"/><circle cx="7" cy="12" r="1.3" fill="#bbb"/><circle cx="14" cy="12" r="1.3" fill="#bbb"/></svg>MY CART <span>- 0.00</span></div>
    <nav class="abs main-nav">
      <a class="active" href="#">Home</a><a href="#">Shop</a><a href="#">Wholesale</a><a href="#">Gallery</a><a href="#">Blog</a><a href="#">Contact</a>
    </nav>
  </header>

  <main>
    <div class="abs feature" role="img" aria-label="Featured photo of pastel gingham ribbons"></div>
    <div class="abs dots"><i class="on"></i><i></i><i></i><i></i><i></i><i></i><i></i><i></i><i></i></div>

    <h2 class="abs section-head" style="font-weight:400">Latest Categories</h2>

    <article class="card" style="left:372px;top:525px">
      <div class="photo" role="img" aria-label="Photo of striped grosgrain ribbons" style="background:linear-gradient(90deg,#d9545a,#a9c98a,#e8d27a,#b9d0dc)"></div>
      <h3>Transport ribbon</h3><p>car, helicopter and truck</p>
      <div class="price">$ 2.50 only</div><div class="btn">View Products</div>
    </article>
    <article class="card" style="left:546px;top:525px">
      <div class="photo" role="img" aria-label="Photo of stacked washi tape rolls" style="background:linear-gradient(#9aa56a,#e7b24a,#e8764a,#e9a07a)"></div>
      <h3>Transport ribbon</h3><p>car, helicopter and truck</p>
      <div class="price">$ 2.50 only</div><div class="btn">View Products</div>
    </article>
    <article class="card" style="left:719px;top:525px">
      <div class="photo" role="img" aria-label="Photo of pink and green fabric flowers" style="background:linear-gradient(135deg,#c8cfb0,#b9858c,#9ebb74)"></div>
      <h3>Transport ribbon</h3><p>car, helicopter and truck</p>
      <div class="price">$ 2.50 only</div><div class="btn">View Products</div>
    </article>

    <div class="abs rule"></div>

    <article class="card" style="left:372px;top:820px">
      <div class="photo" role="img" aria-label="Photo of red and pink fabric flowers" style="background:linear-gradient(135deg,#8e2a34,#c99aa4,#efe6e6)"></div>
      <h3>Transport ribbon</h3><p>car, helicopter and truck</p>
      <div class="price">$ 2.50 only</div><div class="btn">View Products</div>
    </article>
    <article class="card" style="left:546px;top:820px">
      <div class="photo" role="img" aria-label="Photo of pastel gingham ribbons" style="background:linear-gradient(135deg,#e6e0f0,#c6aee6,#f0dc90,#edc4d2)"></div>
      <h3>Transport ribbon</h3><p>car, helicopter and truck</p>
      <div class="price">$ 2.50 only</div><div class="btn">View Products</div>
    </article>
    <article class="card" style="left:719px;top:820px">
      <div class="photo" role="img" aria-label="Photo of striped grosgrain ribbons" style="background:linear-gradient(90deg,#d9545a,#a9c98a,#e8d27a,#b9d0dc)"></div>
      <h3>Transport ribbon</h3><p>car, helicopter and truck</p>
      <div class="price">$ 2.50 only</div><div class="btn">View Products</div>
    </article>
  </main>

  <footer class="abs footer">
    <div class="footer-links">
      <a class="active" href="#">Home</a><a href="#">Shop</a><a href="#">Wholesale</a><a href="#">Gallery</a><a href="#">Blog</a><a href="#">About Stitch Haven</a><a href="#">Contact</a><a href="#">Privacy Policy</a><a href="#">Terms &amp; Conditions</a>
    </div>
    <p class="copyright">Copyright © <b>Stitch Haven</b> 2013.All Right Reserved</p>
  </footer>

</div>
</body>
</html>
```